Interior designer's blog sharing design tips photos and design links

I need a fresh, fun, stylish blog design I love color and texture- I'm an interior designer in NY and want to come across as sophisticated yet approachable. I will be posting interior design photos and products

Target Market(s)

Women 25-54

Industry/Entity Type

Interior

Font styles to use
Serif

Colors
3377b5
886aae
ffc214
fbee3e
ec1f27
e54d9c
a54499

Requirements
Must have
• A space for my image. Link to my website. Friendly. Pixlo and Chirpy accoubts. Color cool fonts

```html
<!DOCTYPE html>
<html lang="en">
<head>
<meta charset="utf-8">
<title>Clara Venn — Interior Designer &amp; Stylist</title>
<link rel="stylesheet" href="https://fonts.googleapis.com/css2?family=Roboto:wght@400;700&family=Roboto+Condensed:wght@400&family=Arimo:wght@400;700&display=swap">
<style>
:root{
  --yellow:#fbee3e;
  --amber:#ffc214;
  --red:#ec1f27;
  --pink:#e54d9c;
  --purple:#886aae;
  --blue:#3377b5;
  --card:#efefef;
  --ink:#4a4a4a;
  --muted:#666;
  --button:#8a8a8a;
}
*{box-sizing:border-box;margin:0;padding:0}
html,body{width:857px;height:1200px;overflow:hidden}
body{
  position:relative;
  font-family:"Arimo",Arial,sans-serif;
  color:var(--ink);
  background:linear-gradient(160deg,#d6e3e5 0%,#e3e8e2 35%,#dfe6e4 60%,#d3e1e6 100%);
}
.topline{position:absolute;left:0;top:0;width:857px;height:6px;background:var(--yellow);z-index:2}
.hero{
  position:absolute;left:0;top:0;width:857px;height:313px;
  background:
    radial-gradient(ellipse at 20% 70%,#e2352e 0%,transparent 55%),
    radial-gradient(ellipse at 80% 30%,#d9433d 0%,transparent 60%),
    linear-gradient(135deg,#e25a58 0%,#d93a35 45%,#e4605a 100%);
}
.hero-band{position:absolute;left:0;top:313px;width:857px;height:30px;background:var(--yellow)}
.avatar{
  position:absolute;left:353px;top:36px;width:151px;height:151px;border-radius:50%;
  border:4px solid #fff;
  background:linear-gradient(160deg,#c9d6e6 0%,#b89682 55%,#e8e2dc 100%);
}
.name{
  position:absolute;left:0;top:205px;width:857px;text-align:center;
  font-family:"Roboto",Arial,sans-serif;font-weight:700;font-size:38px;color:#fff;letter-spacing:.5px;
}
.role{
  position:absolute;left:0;top:248px;width:857px;text-align:center;
  font-family:"Roboto Condensed",Arial,sans-serif;font-size:12px;letter-spacing:2px;color:#fff;
}
.social{position:absolute;left:338px;top:297px;display:flex;gap:6px}
.social a{
  width:31px;height:31px;display:flex;align-items:center;justify-content:center;
  font-family:"Arimo",Arial,sans-serif;font-size:6.5px;font-weight:700;color:#fff;text-decoration:none;
  box-shadow:0 3px 0 var(--amber);
}
.s1{background:var(--ink)} .s2{background:var(--blue)} .s3{background:#3b5b9a} .s4{background:#3a9fd8} .s5{background:var(--red)}

.card{position:absolute;width:184px;background:var(--card);box-shadow:0 1px 2px rgba(0,0,0,.08)}
.card-head{display:flex;height:31px}
.card-icon{width:31px;height:31px;display:flex;align-items:center;justify-content:center;flex:none}
.card-meta{padding:4px 0 0 4px}
.card-title{font-family:"Roboto",Arial,sans-serif;font-size:10.5px;line-height:12px}
.card-stats{font-size:6px;color:var(--muted);margin-top:2px;display:flex;align-items:center;gap:3px}
.card-stats svg{flex:none}
.photo{display:block;margin:6px 6px 0;width:172px;position:relative}
.overlay{position:absolute;left:50%;top:50%;transform:translate(-50%,-50%)}
.card-text{font-size:6px;line-height:7.3px;color:var(--muted);padding:5px 6px 0}
.card-text p+p{margin-top:3px}
.read-more{
  position:absolute;right:6px;bottom:6px;padding:4px 4px;font-size:6px;color:#fff;text-decoration:none;
}
.purple .card-icon{background:var(--purple)} .purple .card-title{color:var(--purple)}
.amber .card-icon{background:var(--amber)} .amber .card-title{color:var(--amber)} .amber .read-more{background:var(--amber)}
.red .card-icon{background:var(--red)} .red .card-title{color:#c3141b} .red .read-more{background:var(--red)}
.pink .card-icon{background:var(--pink)} .pink .card-title{color:var(--pink)} .pink .read-more{background:var(--pink)}
.navy .card-icon{background:var(--purple)} .navy .card-title{color:#3b2f6b}

.ph-sea{background:linear-gradient(180deg,#7d6c50 0%,#8f7f5e 35%,#4c5156 62%,#232632 100%)}
.ph-mugs{background:radial-gradient(ellipse at 40% 70%,#a1482c 0%,transparent 50%),linear-gradient(170deg,#3a2a22 0%,#6e4a33 50%,#4a2e20 100%)}
.ph-dining{background:linear-gradient(180deg,#eceae6 0%,#d9d4cc 50%,#9a6a3e 80%,#7a5230 100%)}
.ph-living{background:linear-gradient(180deg,#ece6dc 0%,#d8cbb8 55%,#8fa3a2 100%)}
.ph-lounge{background:linear-gradient(180deg,#e2dccf 0%,#cfc4b0 50%,#b7c4c4 100%)}
.ph-forest{background:radial-gradient(ellipse at 70% 30%,#5a7a4c 0%,transparent 50%),linear-gradient(180deg,#1e2d2c 0%,#2d3b2e 55%,#6a5a3c 100%)}

.load-more{
  position:absolute;left:370px;top:1034px;width:116px;height:26px;background:var(--button);
  display:flex;align-items:center;justify-content:center;
  font-family:"Roboto",Arial,sans-serif;font-weight:700;font-size:13px;color:#e0e0e0;text-decoration:none;
}
.footer{
  position:absolute;left:0;top:1170px;width:857px;height:30px;background:var(--yellow);
  display:flex;align-items:center;justify-content:center;font-size:9px;color:#222;
}
</style>
</head>
<body>
<header>
  <div class="hero" role="img" aria-label="Red-tinted photo of a designer's desk with rulers, notebooks and a chair"></div>
  <div class="topline"></div>
  <div class="hero-band"></div>
  <div class="avatar" role="img" aria-label="Portrait photo of the designer"></div>
  <h1 class="name">Clara Venn</h1>
  <p class="role">INTERIOR DESIGNER - STYLIST</p>
  <nav class="social">
    <a class="s1" href="#">Pixlo</a>
    <a class="s2" href="#">Linkwork</a>
    <a class="s3" href="#">Friendly</a>
    <a class="s4" href="#">Chirpy</a>
    <a class="s5" href="#">Circlo</a>
  </nav>
</header>

<svg width="0" height="0" style="position:absolute">
  <defs>
    <symbol id="note" viewBox="0 0 20 20"><path d="M7 3 L17 1 V14 A3 2.5 0 1 1 15 11.7 V5 L9 6.2 V16 A3 2.5 0 1 1 7 13.7 Z" fill="#fff"/></symbol>
    <symbol id="eye" viewBox="0 0 10 6"><path d="M0 3 Q5 -2 10 3 Q5 8 0 3Z" fill="#777"/><circle cx="5" cy="3" r="1.3" fill="#efefef"/></symbol>
    <symbol id="bubble" viewBox="0 0 10 8"><path d="M1 1 H9 V5.5 H4 L2 7.5 V5.5 H1Z" fill="#777"/></symbol>
    <symbol id="play" viewBox="0 0 50 50"><circle cx="25" cy="25" r="25" fill="#fff"/><path d="M19 14 L37 25 L19 36Z" fill="#222"/></symbol>
  </defs>
</svg>

<main>
  <article class="card purple" style="left:135px;top:453px;height:205px">
    <div class="card-head">
      <div class="card-icon"><svg width="20" height="20"><use href="#note"/></svg></div>
      <div class="card-meta"><h2 class="card-title">Velvet Hours by Mira</h2>
        <div class="card-stats"><svg width="8" height="5"><use href="#eye"/></svg>1332 views <svg width="7" height="6"><use href="#bubble"/></svg>1332 comments</div></div>
    </div>
    <div class="photo ph-sea" style="height:162px" role="img" aria-label="Lifeguard tower on an empty beach at dusk">
      <svg class="overlay" width="50" height="50"><use href="#play"/></svg>
    </div>
  </article>

  <article class="card red" style="left:135px;top:677px;height:321px">
    <div class="card-head">
      <div class="card-icon"><svg width="20" height="20"><use href="#note"/></svg></div>
      <div class="card-meta"><h2 class="card-title">Kitchen Design</h2>
        <div class="card-stats"><svg width="8" height="5"><use href="#eye"/></svg>1332 views <svg width="7" height="6"><use href="#bubble"/></svg>1332 comments</div></div>
    </div>
    <div class="photo ph-living" style="height:99px" role="img" aria-label="Bright living room with fireplace and patterned armchairs"></div>
    <div class="photo ph-lounge" style="height:124px" role="img" aria-label="Airy lounge with white sofa and long curtains"></div>
    <div class="card-text"><p>A calm living room built on cream sofas, patterned chairs and a low fireplace wall for easy evenings.</p></div>
    <a class="read-more" href="#">Read More</a>
  </article>

  <article class="card amber" style="left:337px;top:453px;height:323px">
    <div class="card-head">
      <div class="card-icon"><svg width="18" height="18" viewBox="0 0 18 18"><circle cx="9" cy="9" r="8" fill="#fff"/><path d="M7 5 L13 9 L7 13Z" fill="var(--amber)"/></svg></div>
      <div class="card-meta"><h2 class="card-title">Interior Design Tutorial</h2>
        <div class="card-stats"><svg width="8" height="5"><use href="#eye"/></svg>1332 views <svg width="7" height="6"><use href="#bubble"/></svg>1332 comments</div></div>
    </div>
    <div class="photo ph-mugs" style="height:225px" role="img" aria-label="Enamel mugs on a wooden table">
      <svg class="overlay" width="80" height="50" viewBox="0 0 80 50"><path d="M0 25 Q40 -18 80 25 Q40 68 0 25Z" fill="#fff"/><circle cx="40" cy="25" r="13" fill="#8a8a8a"/><circle cx="40" cy="25" r="6" fill="#fff"/></svg>
    </div>
    <div class="card-text"><p>Simple ways to warm a room with clay mugs, soft wood tones and a few bright accents for cozy mornings.</p></div>
    <a class="read-more" href="#">Read More</a>
  </article>

  <article class="card navy" style="left:337px;top:794px;height:204px">
    <div class="card-head">
      <div class="card-icon"><svg width="20" height="20"><use href="#note"/></svg></div>
      <div class="card-meta"><h2 class="card-title">Velvet Hours by Mira</h2>
        <div class="card-stats"><svg width="8" height="5"><use href="#eye"/></svg>1332 views <svg width="7" height="6"><use href="#bubble"/></svg>1332 comments</div></div>
    </div>
    <div class="photo ph-sea" style="height:161px" role="img" aria-label="Lifeguard tower on an empty beach at dusk">
      <svg class="overlay" width="50" height="50"><use href="#play"/></svg>
    </div>
  </article>

  <article class="card red" style="left:538px;top:453px;height:205px">
    <div class="card-head">
      <div class="card-icon"><svg width="20" height="20"><use href="#note"/></svg></div>
      <div class="card-meta"><h2 class="card-title">Velvet Hours by Mira</h2>
        <div class="card-stats"><svg width="8" height="5"><use href="#eye"/></svg>1332 views <svg width="7" height="6"><use href="#bubble"/></svg>1332 comments</div></div>
    </div>
    <div class="photo ph-dining" style="height:162px" role="img" aria-label="Dining room with white chairs around a wooden table"></div>
  </article>

  <article class="card pink" style="left:538px;top:677px;height:321px">
    <div class="card-head">
      <div class="card-icon"><svg width="20" height="20"><use href="#note"/></svg></div>
      <div class="card-meta"><h2 class="card-title">Kitchen Design</h2>
        <div class="card-stats"><svg width="8" height="5"><use href="#eye"/></svg>1332 views <svg width="7" height="6"><use href="#bubble"/></svg>1332 comments</div></div>
    </div>
    <div class="photo ph-forest" style="height:117px" role="img" aria-label="Person sitting in a pine forest"></div>
    <div class="card-text">
      <p>Forest greens and deep browns bring the outdoors inside. Pair them with linen, raw oak and matte black hardware for a kitchen that feels grounded and quietly bold every single day.</p>
      <p>Start with one statement wall, then layer open shelving, woven baskets and trailing plants. Keep counters clear so the colour can breathe and the room stays easy to use.</p>
      <p>Finish with warm lighting low over the table and a soft runner underfoot.</p>
      <p>Small changes, big welcome.</p>
    </div>
    <a class="read-more" href="#">Read More</a>
  </article>

  <a class="load-more" href="#">LOAD MORE</a>
</main>

<footer class="footer">Copyright © 2015 RoomStory</footer>
</body>
</html>
```